Logo and business card for optometric practice
Calvin Mortenhall & Associates
Petra Valunkova, O.D.
Simon Orchardt, O.D.
Neil Tabarrou, O.D.
417 Meadowbrook Parkway
Ashfield Terrace, New York 11498
516-555-0142

Target Market(s)

Patients, general public

Industry/Entity Type

Business

Logo Text

Calvin Mortenhall & Associates Optometrists

Logo styles of interest
Pictorial/Combination Logo
Font styles to use
Serif
Sans Serif

Requirements
Must have
• current inspiration: realistic or photo closeup of eye, with interesting treatment of the iris OR
tech look, with closeup of eye and grid like the doctor is looking through a camera or microscope to view the eye up close
Should not have
• NO cartoons

```html
<!DOCTYPE html>
<html lang="en">
<head>
<meta charset="utf-8">
<title>Calvin Mortenhall &amp; Associates — Identity</title>
<link href="https://fonts.googleapis.com/css2?family=Cinzel:wght@400;500&family=Open+Sans:wght@400&display=swap" rel="stylesheet">
<style>
  :root{
    --ink:#111111;
    --paper:#ffffff;
    --card:#fbfbfb;
    --sky:#3fb2e2;
    --teal-dark:#0b4f6c;
    --teal-mid:#1a7398;
    --shine:#9fd6ee;
    --ghost:#eeeeee;
    --shadow:rgba(0,0,0,.35);
  }
  *{margin:0;padding:0;box-sizing:border-box}
  html,body{width:1200px;height:1000px;overflow:hidden;background:var(--paper)}
  .canvas{position:relative;width:1200px;height:1000px;font-family:"Cinzel",serif;color:var(--ink)}
  .brand{position:absolute;display:flex;flex-direction:column;align-items:center;text-align:center;color:var(--ink);font-family:"Cinzel",serif;font-weight:400}
  .brand__dot{border-radius:50%;background:var(--ink)}
  .brand__name{line-height:1.25;letter-spacing:.06em;white-space:nowrap}
  .brand--main{left:265px;top:70px;width:600px}
  .brand--main .brand__dot{width:90px;height:90px;margin-bottom:28px}
  .brand--main .brand__name{font-size:30px}
  .sheet{position:absolute;background:var(--card);box-shadow:0 1px 4px var(--shadow);overflow:hidden}
  .sheet svg.swoosh{position:absolute;left:0;bottom:0}
  .card-front{left:212px;top:465px;width:308px;height:185px}
  .card-front .brand{left:0;top:22px;width:308px}
  .card-front .brand__dot{width:30px;height:30px;margin-bottom:10px}
  .card-front .brand__name{font-size:15px}
  .card-back{left:212px;top:680px;width:308px;height:185px}
  .card-back .corner-dot{position:absolute;left:-30px;top:-30px;width:60px;height:60px;border-radius:50%;background:var(--ink)}
  .staff{position:absolute;left:113px;top:20px;list-style:none;font-size:12.5px;line-height:19px;letter-spacing:.02em;white-space:nowrap}
  .contact{position:absolute;left:114px;font-family:"Open Sans",sans-serif;font-size:8px;line-height:10px;display:flex;gap:9px;white-space:nowrap}
  .contact svg{flex:none}
  .contact--phone{top:100px}
  .contact--address{top:118px}
  .letterhead{left:715px;top:388px;width:412px;height:582px;background:var(--paper)}
  .letterhead .brand{left:56px;top:22px;width:300px}
  .letterhead .brand__dot{width:24px;height:24px;margin-bottom:8px}
  .letterhead .brand__name{font-size:12px}
  .letterhead .watermark{position:absolute;left:176px;top:268px;width:82px;height:82px;border-radius:50%;background:var(--ghost)}
  .letterhead .staff{left:20px;top:476px;font-size:6.5px;line-height:8.5px}
  .letterhead .contact{left:20px;font-size:4.5px;line-height:5.5px;gap:6px}
  .letterhead .contact--phone{top:512px}
  .letterhead .contact--address{top:523px}
</style>
</head>
<body>
<main class="canvas">
  <svg width="0" height="0" style="position:absolute" aria-hidden="true">
    <defs>
      <linearGradient id="steel" x1="0" y1="0" x2="1" y2="0">
        <stop offset="0" stop-color="#0b4f6c"/>
        <stop offset=".35" stop-color="#1a7398"/>
        <stop offset=".55" stop-color="#9fd6ee"/>
        <stop offset=".7" stop-color="#1a7398"/>
        <stop offset="1" stop-color="#0b4f6c"/>
      </linearGradient>
    </defs>
  </svg>

  <div class="brand brand--main">
    <span class="brand__dot"></span>
    <span class="brand__name">Calvin Mortenhall<br>&amp; Associates Optometrists</span>
  </div>

  <section class="sheet card-front">
    <div class="brand">
      <span class="brand__dot"></span>
      <span class="brand__name">Calvin Mortenhall<br>&amp; Associates Optometrists</span>
    </div>
    <svg class="swoosh" width="308" height="60" viewBox="0 125 308 60">
      <path d="M0,157 Q160,152 308,124 L308,185 L0,185Z" fill="var(--sky)"/>
      <path d="M0,171 Q180,165 308,128 L308,185 L0,185Z" fill="url(#steel)"/>
      <path d="M0,169 Q180,162 308,127" fill="none" stroke="#fff" stroke-width="2"/>
    </svg>
  </section>

  <section class="sheet card-back">
    <span class="corner-dot"></span>
    <ul class="staff">
      <li>Petra Valunkova, O.D.</li>
      <li>Simon L. Orchardt, O.D.</li>
      <li>Neil A. Tabarrou, O.D.</li>
      <li>Marta Quillen, Optician</li>
    </ul>
    <div class="contact contact--phone">
      <svg width="7" height="10" viewBox="0 0 7 10"><rect x=".6" y=".6" width="5.8" height="8.8" rx="1.2" fill="none" stroke="var(--ink)" stroke-width="1.2"/></svg>
      <span>516-555-0142</span>
    </div>
    <div class="contact contact--address">
      <svg width="11" height="9" viewBox="0 0 11 9"><path d="M5.5 0 L11 4.5 H9.5 V9 H1.5 V4.5 H0Z" fill="var(--ink)"/></svg>
      <span>417 Meadowbrook Parkway<br>Ashfield Terrace, New York 11498</span>
    </div>
    <svg class="swoosh" width="308" height="60" viewBox="0 125 308 60">
      <path d="M0,128 Q150,140 308,168 L308,185 L0,185Z" fill="url(#steel)"/>
      <path d="M150,150 Q240,160 308,160 L308,171 Q230,166 150,152Z" fill="var(--sky)"/>
      <path d="M0,131 Q150,143 308,166" fill="none" stroke="#fff" stroke-width="2"/>
    </svg>
  </section>

  <section class="sheet letterhead">
    <div class="brand">
      <span class="brand__dot"></span>
      <span class="brand__name">Calvin Mortenhall<br>&amp; Associates Optometrists</span>
    </div>
    <span class="watermark"></span>
    <ul class="staff">
      <li>Petra Valunkova, O.D.</li>
      <li>Simon L. Orchardt, O.D.</li>
      <li>Neil A. Tabarrou, O.D.</li>
      <li>Marta Quillen, Optician</li>
    </ul>
    <div class="contact contact--phone">
      <svg width="4" height="6" viewBox="0 0 7 10"><rect x=".6" y=".6" width="5.8" height="8.8" rx="1.2" fill="none" stroke="var(--ink)" stroke-width="1.4"/></svg>
      <span>516-555-0142</span>
    </div>
    <div class="contact contact--address">
      <svg width="6" height="5" viewBox="0 0 11 9"><path d="M5.5 0 L11 4.5 H9.5 V9 H1.5 V4.5 H0Z" fill="var(--ink)"/></svg>
      <span>417 Meadowbrook Parkway<br>Ashfield Terrace, New York 11498</span>
    </div>
    <svg class="swoosh" width="412" height="70" viewBox="0 512 412 70">
      <path d="M0,548 Q230,548 412,514 L412,582 L0,582Z" fill="var(--sky)"/>
      <path d="M0,566 Q250,560 412,520 L412,582 L0,582Z" fill="url(#steel)"/>
      <path d="M0,562 Q250,556 412,518" fill="none" stroke="#fff" stroke-width="2.5"/>
    </svg>
  </section>
</main>
</body>
</html>
```